Business cards

Design business cards for our company. Just a straight, business like design with the logo, name, function and contact details

Target Market(s)

We are a innovative technological company active in water treatment

Industry/Entity Type

Water management

Contact Information for Business Card

Name, Function, email, telephone number, link to website

```html
<!DOCTYPE html>
<html lang="en">
<head>
<meta charset="utf-8">
<title>Tidewell – Business Cards</title>
<link href="https://fonts.googleapis.com/css2?family=Lato:wght@400;700&family=Lora:wght@600&display=swap" rel="stylesheet">
<style>
  :root{
    --bg:#e9ebee;
    --blue:#2a93d5;
    --blue-deep:#0a3f5f;
    --blue-mid:#1d6e9f;
    --grey:#7a7d80;
    --text:#4a4d50;
    --rule:#9a9da0;
    --white:#ffffff;
  }
  *{box-sizing:border-box;margin:0;padding:0}
  html,body{width:1200px;height:900px;overflow:hidden}
  body{
    background:var(--bg);
    font-family:"Lato",sans-serif;
    position:relative;
  }
  .card{
    position:absolute;
    width:600px;height:343px;
    box-shadow:0 10px 30px rgba(0,0,0,.18);
    overflow:hidden;
  }
  /* back side */
  .card-back{
    left:300px;top:50px;
    background:radial-gradient(ellipse at 50% 60%, #2b95d1 0%, var(--blue-mid) 40%, var(--blue-deep) 100%);
    color:var(--white);
  }
  .card-back .brand{
    position:absolute;left:0;right:0;top:118px;
    display:flex;align-items:center;justify-content:center;gap:12px;
    font-weight:700;font-size:30px;letter-spacing:1px;
  }
  .brand-dot{width:16px;height:16px;border-radius:50%;background:currentColor;display:inline-block}
  .card-back .rule{
    position:absolute;left:100px;right:100px;top:200px;
    height:1px;background:rgba(200,210,220,.6);
  }
  .card-back .web{
    position:absolute;left:0;right:0;top:214px;text-align:center;
    font-family:"Lora",serif;font-weight:600;font-size:18px;letter-spacing:7px;
  }
  /* front side */
  .card-front{
    left:300px;top:470px;
    background:linear-gradient(135deg,#ffffff 0%,#f1f1f1 100%);
    color:var(--text);
  }
  .card-front .brand{
    position:absolute;left:0;right:0;top:42px;
    display:flex;align-items:center;justify-content:center;gap:12px;
    color:var(--blue);font-weight:700;font-size:40px;letter-spacing:1px;
  }
  .card-front .rule{position:absolute;height:1px;background:var(--rule)}
  .rule-top{left:150px;right:40px;top:128px}
  .rule-bottom{left:40px;right:150px;top:232px}
  .identity{
    position:absolute;left:0;right:0;top:152px;text-align:center;
    font-size:20px;
  }
  .identity .name{color:var(--blue);font-weight:700;letter-spacing:.5px}
  .identity .sep{color:var(--blue);margin:0 8px}
  .identity .role{color:var(--grey)}
  .contact-left{
    position:absolute;left:46px;top:246px;font-size:15px;line-height:22px;
  }
  .contact-left .row{display:flex;align-items:flex-start;gap:10px}
  .contact-left svg{width:16px;height:16px;margin-top:3px;fill:var(--blue);flex:none}
  .contact-left .indent{padding-left:26px}
  .contact-right{
    position:absolute;right:38px;top:178px;font-size:15px;line-height:24px;text-align:right;
  }
  .contact-right .row{display:flex;align-items:center;justify-content:flex-end;gap:8px}
  .contact-right svg{width:16px;height:16px;flex:none}
  .band{position:absolute;left:0;right:0;bottom:0;height:12px;background:var(--blue)}
</style>
</head>
<body>

<section class="card card-back" aria-label="Business card, reverse side">
  <div class="brand"><span class="brand-dot"></span>Tidewell</div>
  <div class="rule"></div>
  <div class="web">www.tidewell.com</div>
</section>

<section class="card card-front" aria-label="Business card, front side">
  <div class="brand"><span class="brand-dot"></span>Tidewell</div>
  <div class="rule rule-top"></div>
  <p class="identity"><span class="name">MAREN HOLT</span><span class="sep">|</span><span class="role">CEO</span></p>
  <div class="rule rule-bottom"></div>

  <div class="contact-left">
    <div class="row">
      <svg viewBox="0 0 24 24" aria-hidden="true"><path d="M6.6 10.8a15.1 15.1 0 0 0 6.6 6.6l2.2-2.2a1 1 0 0 1 1-.25 11.4 11.4 0 0 0 3.6.57 1 1 0 0 1 1 1V20a1 1 0 0 1-1 1A17 17 0 0 1 3 4a1 1 0 0 1 1-1h3.5a1 1 0 0 1 1 1c0 1.25.2 2.45.57 3.57a1 1 0 0 1-.25 1z"/></svg>
      <span>+31 612048117</span>
    </div>
    <div class="row">
      <svg viewBox="0 0 24 24" aria-hidden="true"><path d="M12 2a7 7 0 0 0-7 7c0 5.2 7 13 7 13s7-7.8 7-13a7 7 0 0 0-7-7zm0 9.5A2.5 2.5 0 1 1 12 6.5a2.5 2.5 0 0 1 0 5z"/></svg>
      <span>Duinlaan 14 2201 KB Zeestrand</span>
    </div>
    <div class="indent">The Netherlands</div>
  </div>

  <div class="contact-right">
    <div class="row">
      <span>info@tidewell.com</span>
      <svg viewBox="0 0 24 24" aria-hidden="true"><rect x="2" y="5" width="20" height="14" fill="#2a93d5"/><path d="M2 5l10 8 10-8" fill="none" stroke="#fff" stroke-width="1.8"/></svg>
    </div>
    <div class="row">
      <span>www.tidewell.com</span>
      <svg viewBox="0 0 24 24" aria-hidden="true" fill="none" stroke="#2a93d5" stroke-width="1.8"><circle cx="12" cy="12" r="9.5"/><ellipse cx="12" cy="12" rx="4" ry="9.5"/><path d="M2.5 12h19M4 7h16M4 17h16"/></svg>
    </div>
  </div>

  <div class="band"></div>
</section>

</body>
</html>
```